New business logo / Business Card Design

My company provides Interim Management and consultancy, for Facilities Services. Covers any aspect of facilities management, including M&E, helpdesk, asset management, supplier relationships, catering, cleaning etc. Company provides innovative solutions to exceed client needs, drawing on years of experience. Initial thoughts on logo are attached below. Fits with RAG status on projects, red, amber and green, with logo design colours around moving services from amber to green.

Target Market(s)

Facilities Management clients and service providers

Industry/Entity Type

Business

Contact Information for Business Card

Company Name = k7Rventures Ltd My name on card = Derek Whitcombe, Director Mobile = 07516309842 Email = Derek@k7rventuresltd.co.uk Twitter = @k7Rventures Ltd

Font styles to use
Sans Serif

Colors
f37122
00a990

Requirements
Must have
• Logo to be evident, with some background image in reference to Facilities Management

```html
<!DOCTYPE html>
<html lang="en">
<head>
<meta charset="utf-8">
<title>k7Rventures Ltd — Business Card</title>
<link href="https://fonts.googleapis.com/css2?family=Montserrat:wght@400;500;700&display=swap" rel="stylesheet">
<style>
  :root {
    --backdrop: #e8e5e1;
    --card: #ffffff;
    --ink: #161616;
    --brand-green: #1b6a36;
    --brand-orange: #f26a21;
    --rule: #2a2a2a;
  }
  * { margin: 0; padding: 0; box-sizing: border-box; }
  html, body {
    width: 1200px;
    height: 1000px;
    overflow: hidden;
    background: var(--backdrop);
    font-family: "Montserrat", Arial, sans-serif;
  }
  .canvas { position: relative; width: 1200px; height: 1000px; }
  .card {
    position: absolute;
    left: 265px;
    width: 666px;
    height: 397px;
    background: var(--card);
    box-shadow: 0 4px 10px rgba(0,0,0,0.18);
  }
  .card--front { top: 73px; }
  .card--back { top: 532px; }
  .wordmark {
    position: absolute;
    right: 32px;
    top: 84px;
    font-weight: 700;
    font-size: 40px;
    letter-spacing: 0.5px;
    color: var(--ink);
    white-space: nowrap;
  }
  .holder-name {
    position: absolute;
    left: 33px;
    top: 225px;
    font-size: 26px;
    font-weight: 400;
    color: var(--brand-green);
  }
  .holder-role {
    position: absolute;
    left: 33px;
    top: 259px;
    font-size: 16px;
    color: var(--brand-orange);
  }
  .divider {
    position: absolute;
    left: 33px;
    right: 32px;
    top: 288px;
    height: 1.5px;
    background: var(--rule);
  }
  .contacts {
    position: absolute;
    left: 33px;
    right: 32px;
    top: 325px;
    display: flex;
    justify-content: space-between;
    align-items: center;
    font-size: 15.5px;
    color: var(--ink);
  }
  .contact { display: flex; align-items: center; gap: 7px; white-space: nowrap; }
  .contact svg { display: block; fill: var(--brand-green); }
  .band {
    position: absolute;
    bottom: 0;
    height: 10px;
  }
  .band--amber { left: 0; width: 331px; background: var(--brand-orange); }
  .band--green { right: 0; width: 331px; background: var(--brand-green); }
</style>
</head>
<body>
<div class="canvas">
  <section class="card card--front">
    <div class="wordmark">k7Rventures Ltd</div>
    <div class="holder-name">Derek Whitcombe</div>
    <div class="holder-role">Director</div>
    <div class="divider"></div>
    <div class="contacts">
      <span class="contact">
        <svg width="15" height="12" viewBox="0 0 15 12" aria-hidden="true"><path d="M1 3c0-1.5 2.5-2.5 6.5-2.5S14 1.5 14 3v1.2h-3V3H4v1.2H1z"/><path d="M3.5 5h8l2 5.5H1.5z"/></svg>
        07516309842
      </span>
      <span class="contact">
        <svg width="14" height="10" viewBox="0 0 14 10" aria-hidden="true"><rect width="14" height="10"/><path d="M1 1l6 4.5L13 1" fill="none" stroke="#fff" stroke-width="1.3"/></svg>
        Derek@k7rventuresltd.co.uk
      </span>
      <span class="contact">
        <svg width="12" height="12" viewBox="0 0 12 12" aria-hidden="true"><circle cx="6" cy="6" r="5.5"/></svg>
        @k7Rventures Ltd
      </span>
    </div>
    <div class="band band--amber"></div>
    <div class="band band--green"></div>
  </section>

  <section class="card card--back">
    <div class="wordmark">k7Rventures Ltd</div>
    <div class="holder-name">Derek Whitcombe</div>
    <div class="holder-role">Director</div>
    <div class="divider"></div>
    <div class="contacts">
      <span class="contact">
        <svg width="15" height="12" viewBox="0 0 15 12" aria-hidden="true"><path d="M1 3c0-1.5 2.5-2.5 6.5-2.5S14 1.5 14 3v1.2h-3V3H4v1.2H1z"/><path d="M3.5 5h8l2 5.5H1.5z"/></svg>
        07516309842
      </span>
      <span class="contact">
        <svg width="14" height="10" viewBox="0 0 14 10" aria-hidden="true"><rect width="14" height="10"/><path d="M1 1l6 4.5L13 1" fill="none" stroke="#fff" stroke-width="1.3"/></svg>
        Derek@k7rventuresltd.co.uk
      </span>
      <span class="contact">
        <svg width="12" height="12" viewBox="0 0 12 12" aria-hidden="true"><circle cx="6" cy="6" r="5.5"/></svg>
        @k7Rventures Ltd
      </span>
    </div>
    <div class="band band--amber"></div>
    <div class="band band--green"></div>
  </section>
</div>
</body>
</html>
```